halbrook paving works

Needs to have phone number 0418352790 and email carlwhitby@mailnest.com.au.
ABN 27813046652
name carl whitby

For all your concreting solutions
Excavation
Exposed & colour concrete
House & shed slabs
Driveways
Landing & steps

Contact Information for Business Card

ph 0418352790
email carlwhitby@mailnest.com.au.
ABN 27813046652
name carl whitby

```html
<!DOCTYPE html>
<html lang="en">
<head>
<meta charset="utf-8">
<title>Halbrook Paving Works – Business Card</title>
<link href="https://fonts.googleapis.com/css2?family=Montserrat:wght@500;600&family=Arimo:wght@700&display=swap" rel="stylesheet">
<style>
  :root {
    --backdrop: #bcbdbf;
    --orange: #f26924;
    --white: #ffffff;
    --slate: #666666;
    --ink: #000000;
  }
  * { margin: 0; padding: 0; box-sizing: border-box; }
  html, body { width: 1019px; height: 1200px; overflow: hidden; background: var(--backdrop); }
  .canvas { position: relative; width: 1019px; height: 1200px; }

  .card { position: absolute; left: 77px; width: 869px; height: 531px; overflow: hidden; }
  .card--front { top: 29px; background: var(--orange); }
  .card--back { top: 660px; background: var(--white); }

  .front-wedge { position: absolute; inset: 0; width: 869px; height: 531px; }

  .front-mark {
    position: absolute; left: 118px; top: 219px; width: 120px; height: 120px;
    background: var(--slate);
  }

  .front-title {
    position: absolute; right: 34px; top: 48px;
    font-family: "Montserrat", sans-serif; font-weight: 600;
    font-size: 47px; letter-spacing: -0.5px; color: var(--white); white-space: nowrap;
  }

  .contact-row {
    position: absolute; right: 45px; display: flex; align-items: center; gap: 13px;
    font-family: "Arimo", sans-serif; font-weight: 700; font-size: 21px; color: var(--white);
  }
  .contact-row--phone { top: 198px; }
  .contact-row--email { top: 275px; }
  .contact-icon { width: 54px; height: 54px; flex: none; }

  .lockup-mark {
    position: absolute; left: 172px; top: 212px; width: 110px; height: 110px;
    background: var(--orange);
  }
  .lockup-divider {
    position: absolute; left: 325px; top: 187px; width: 2px; height: 159px; background: var(--orange);
  }
  .lockup-name {
    position: absolute; left: 341px; top: 224px;
    font-family: "Montserrat", sans-serif; font-weight: 600; font-size: 27px;
    letter-spacing: -0.5px; color: var(--orange); white-space: nowrap;
  }
  .lockup-rule {
    position: absolute; left: 341px; top: 268px; width: 86px; height: 2px; background: var(--slate);
  }
  .lockup-phone {
    position: absolute; left: 444px; top: 256px;
    font-family: "Montserrat", sans-serif; font-weight: 500; font-size: 24px;
    letter-spacing: 3px; color: var(--orange);
  }
</style>
</head>
<body>
<main class="canvas">
  <section class="card card--front">
    <svg class="front-wedge" viewBox="0 0 869 531" aria-hidden="true">
      <path d="M0 0 H27 L351 188 C398 214 430 330 346 382 L87 531 H0 Z" fill="var(--white)"/>
    </svg>
    <div class="front-mark" aria-hidden="true"></div>
    <h1 class="front-title">HALBROOK PAVING</h1>
    <div class="contact-row contact-row--phone">
      <span>0418352790</span>
      <svg class="contact-icon" viewBox="0 0 54 54" aria-hidden="true">
        <circle cx="27" cy="27" r="27" fill="var(--ink)"/>
        <path d="M19 14 c2-1 4 0 5 2 l2 5 c1 2 0 3-1 4 l-2 2 c2 4 5 7 9 9 l2-2 c1-1 2-2 4-1 l5 2 c2 1 3 3 2 5 l-1 2 c-2 3-6 3-10 1 c-7-3-13-9-16-16 c-2-4-2-8 1-10 z" fill="var(--white)"/>
      </svg>
    </div>
    <div class="contact-row contact-row--email">
      <span>carlwhitby@mailnest.com.au</span>
      <svg class="contact-icon" viewBox="0 0 54 54" aria-hidden="true">
        <circle cx="27" cy="27" r="27" fill="var(--ink)"/>
        <path d="M14 20 h26 v15 a2 2 0 0 1-2 2 h-22 a2 2 0 0 1-2-2 z" fill="var(--white)"/>
        <path d="M14 20 l13 10 l13-10" fill="none" stroke="var(--ink)" stroke-width="2"/>
      </svg>
    </div>
  </section>

  <section class="card card--back">
    <div class="lockup-mark" aria-hidden="true"></div>
    <div class="lockup-divider" aria-hidden="true"></div>
    <h2 class="lockup-name">HALBROOK PAVING WORKS</h2>
    <div class="lockup-rule" aria-hidden="true"></div>
    <p class="lockup-phone">0418352790</p>
  </section>
</main>
</body>
</html>
```